Broschüre für Beratung, Planung, und Serviceerbringung für Bauprojekte von industriellen und öffentlichen Auftraggebern
Zielgruppe
Die KDR | Group ist eine mittelständige und überregional tätige Unternehmensgruppe, deren Schwerpunkt die Beratung, Planung, und Serviceerbringung für Bauprojekte von industriellen und öffentlichen Auftraggebern ist.
KDR ist seit mehr als 30 Jahren ein kompetenter Ansprechpartner für alle Bereiche der Bautechnik sowie damit zusammenhängenden Fachplanungen und begleitet mit seinen mehr als 50 festangestellten Mitarbeitern die Kunden vom Projektstart über die Planungs-, die Projektvorbereitungs- und Bauphase bis zum „Einzug“ bzw. zur Inbetriebnahme.
Ziel der KDR | Group ist es, gemeinsam mit dem Kunden einen reibungslosen und erfolgreichen Projektablauf sicherzustellen und abzuschließen.
Mit den Anforderungen der Kunden hat sich KDR zu einem überregional tätigen Ingenieur- und Servicedienstleister entwickelt, dessen Geschäftsführung, Verwaltung einschl. IT- Development & Support, in Falkenried ansässig ist.
Am Standort Falkenried befindet sich auch ein technischer Bürostandort, der schwerpunktmäßig Projekte im Kreis Haselbrunn-Eichtal bearbeitet aber auch eng mit den weiteren Bürostandorten in Kornstedt, Sommerfeld an der Lohe-Brückau, Tellborn und Marienquell vernetzt ist und zusammenarbeitet.
Aufgabenstellung
Eine moderne Firmenbroschüre, Bilder sind einige vorhanden

```html
<!DOCTYPE html>
<html lang="de">
<head>
<meta charset="utf-8">
<title>KDR Ingenieurgesellschaft mbH – Broschüre</title>
<link href="https://fonts.googleapis.com/css2?family=Montserrat:wght@600;700;800&family=Raleway:wght@400;500;700&display=swap" rel="stylesheet">
<style>
  :root{
    --backdrop:#4d4d4f;
    --paper:#f4f4f4;
    --paper-shade:#dcdcdc;
    --taupe:#8a8178;
    --taupe-dark:#756c63;
    --taupe-light:#b3aca4;
    --text:#6f6a66;
    --muted:#b9b5b1;
    --white:#ffffff;
  }
  *{margin:0;padding:0;box-sizing:border-box}
  html,body{width:1200px;height:850px;overflow:hidden;background:var(--backdrop)}
  .spread{position:absolute;left:40px;top:30px;width:1120px;height:790px;display:flex;box-shadow:0 10px 30px rgba(0,0,0,.35)}
  .page{position:relative;width:560px;height:790px;overflow:hidden;font-family:'Raleway',sans-serif;color:var(--text)}
  .page--left{background:linear-gradient(90deg,var(--paper) 0%,var(--paper) 85%,var(--paper-shade) 100%)}
  .page--right{background:linear-gradient(90deg,var(--paper-shade) 0%,var(--paper) 12%,var(--paper) 100%)}
  .wave{position:absolute;left:0;top:0;width:560px}
  .intro{position:absolute;left:40px;top:40px;width:470px;color:var(--white)}
  .section-title{font-family:'Montserrat',sans-serif;font-weight:800;text-transform:uppercase;font-size:27px;letter-spacing:.5px}
  .intro .section-title{color:var(--white)}
  .intro-sub{font-family:'Montserrat',sans-serif;font-weight:700;font-size:18px;margin:4px 0 14px}
  .intro p{font-size:11.5px;line-height:1.5;margin-bottom:9px;color:#f1eeeb}
  .intro strong{font-weight:700;color:var(--white)}
  .regional{position:absolute;left:40px;top:432px;width:480px}
  .regional .section-title{color:var(--taupe)}
  .regional p{font-size:12px;line-height:1.5;margin-top:10px}
  .map{position:absolute;left:215px;top:634px;width:290px;height:136px;background:linear-gradient(135deg,#b9d3a4 0%,#cfd9a9 45%,#d9c99a 100%)}
  .photo{position:absolute;left:0;top:0;width:560px;height:270px;background:linear-gradient(120deg,#3e4d5c 0%,#8fa3b5 40%,#c7ced8 60%,#9c7e8f 100%)}
  .services{position:absolute;left:40px;top:318px;width:490px}
  .services .section-title{color:var(--taupe)}
  .services .lead{font-size:10.5px;line-height:1.5;margin:10px 0 12px}
  .services strong{font-weight:700;color:var(--taupe-dark)}
  .group-title{font-family:'Montserrat',sans-serif;font-weight:700;font-size:12.5px;color:var(--muted);margin:10px 0 5px}
  .service-list{list-style:none}
  .service-list li{position:relative;padding-left:16px;font-size:11px;line-height:1.5}
  .service-list li::before{content:"";position:absolute;left:0;top:6px;width:6px;height:6px;border-radius:50%;background:var(--taupe)}
  .page-number{position:absolute;bottom:14px;right:24px;font-size:8px;color:var(--text)}
</style>
</head>
<body>
<main class="spread">
  <section class="page page--left">
    <svg class="wave" height="440" viewBox="0 0 560 440" aria-hidden="true">
      <path d="M0 0H560V270C420 300 280 300 0 420Z" fill="var(--taupe-light)"/>
      <path d="M0 0H560V245C410 270 260 300 0 400Z" fill="var(--taupe)"/>
    </svg>
    <div class="intro">
      <h1 class="section-title">Wir über uns</h1>
      <h2 class="intro-sub">KDR Ingenieurgesellschaft mbH stellt sich vor</h2>
      <p>Wir sind ein mittelständiges und überregional tätiges Ingenieurbüro für Industrie-, <strong>Kommunal- und Gewerbebau.</strong></p>
      <p>Seit mehr als 30 Jahren sind wir ein kompetenter Ansprechpartner für alle Bereiche der Bautechnik und damit zusammenhängenden Fachplanungen.</p>
      <p>Dabei unterstützen und beraten wir Sie als unseren Kunden über den gesamten Projektverlauf hinweg.</p>
      <p>Vom Projektstart bis zum Abschluss:<br>Wir sorgen für einen reibungslosen und erfolgreichen Ablauf Ihres Bauvorhabens.</p>
    </div>
    <div class="regional">
      <h2 class="section-title">Überregional tätig</h2>
      <p>Mit den Anforderungen die an uns gestellt wurden, hat sich unser Unternehmen zu einem überregional tätigen Ingenieurbüro entwickelt. Neben der Verwaltung und dem Büro Haselbrunn-Eichtal in Falkenried unterhalten wir weitere Büros in Sommerfeld an der Lohe-Brückau, in Tellborn, in Kornstedt und in Marienquell am Rhein.</p>
      <p>Unsere Leistungsfähigkeit haben wir in zahlreichen Projekten unter Beweis stellen können.</p>
    </div>
    <div class="map" role="img" aria-label="Landkarte der Region mit den Bürostandorten Kornstedt, Falkenried, Sommerfeld an der Lohe-Brückau, Tellborn und Marienquell"></div>
    <span class="page-number">1</span>
  </section>

  <section class="page page--right">
    <div class="photo" role="img" aria-label="Foto einer Industriehalle mit glänzenden Lüftungs- und Rohrleitungen"></div>
    <svg class="wave" height="330" viewBox="0 0 560 330" aria-hidden="true">
      <path d="M0 330C120 250 300 215 560 205V330Z" fill="var(--paper)"/>
      <path d="M0 330C110 255 290 205 560 190V215C310 222 140 258 0 330Z" fill="var(--taupe)"/>
    </svg>
    <div class="services">
      <h2 class="section-title">Unsere Leistungen</h2>
      <p class="lead">Bauprojekte haben in der Regel eine hohe Komplexität; kein Projekt ist wie das andere. Mit der <strong>KDR Ingenieurgesellschaft mbH</strong> treffen Sie eine gute Wahl, wenn es um die Umsetzung der folgenden Leistungsbereiche geht:</p>
      <h3 class="group-title">Objektplanung gem. HOAI</h3>
      <ul class="service-list">
        <li>Gebäude und Innenräume</li>
        <li>Freianlagen</li>
        <li>Ingenieurbauwerke</li>
        <li>Verkehrsanlagen</li>
      </ul>
      <h3 class="group-title">Fachplanungen gem. HOAI und besondere Leistungen</h3>
      <ul class="service-list">
        <li>Tragwerksplanung</li>
        <li>Thermische Bauphysik</li>
        <li>Schallschutz</li>
        <li>Technische Ausrüstung HKLS Anlagen</li>
        <li>Technische Ausrüstung Elektrotechnische Anlagen</li>
        <li>Technische Ausrüstung EMSR</li>
        <li>Technische Ausrüstung – Sicherheitstechnische Anlagen</li>
        <li>Fabrikplanung</li>
        <li>Leistungen für Thermische Bauphysik</li>
        <li>Brandschutzplanung</li>
        <li>Bundes-Immissionsschutzgesetz (BImSchG)</li>
        <li>Wasserhaushaltsgesetz (WHG)</li>
        <li>Betonerhaltung und -sanierung</li>
        <li>Verordnung über Anlagen zum Umgang mit wassergefährdenden Stoffen (AwSV)</li>
      </ul>
    </div>
    <span class="page-number">2</span>
  </section>
</main>
</body>
</html>
```